Lanterne architecture business cards

We are a new company based in New Zealand. We Specialize in High end Luxury Residential Architecture.

Every home is bespoke and is designed to each clients individual requirements and needs.

I like to design buildings that inspire people through light and form while offering a high level of comfort and usability.

Lines of sight, proportion and balance are fundamental to the spaces I create.
Updates

August 5th is current deadline - Today's date is the 13th of August.

Target Market(s)

New Zealanders who want a custom individual home design, typically 30-65 year old males and females

Industry/Entity Type

Architecture

Contact Information for Business Card

Director - Derek Tolson
Contact Number - 0279164073
Email - info@lanternearchitecture-example.co.nz
Webstie - www.lanternearchitecture-example.co.nz
Social Media - @lanternearchitecture

Font styles to use
Sans Serif

Requirements
Must have
• Logo (Both Sides)
Website
Email
Contact Number
Social Media

Nice to have
• Texture
Should not have
• More than 3 colours - typically I would've thought 2 would be good to match the logo.

```html
<!DOCTYPE html>
<html lang="en">
<head>
<meta charset="utf-8">
<title>Lanterne architecture — business cards</title>
<link rel="stylesheet" href="https://fonts.googleapis.com/css2?family=Josefin+Sans:wght@300;400&family=PT+Sans+Narrow:wght@400;700&display=swap">
<style>
  :root {
    --backdrop: #1f1f1f;
    --card-black: #141414;
    --card-white: #ffffff;
    --gold: #d9a21b;
    --ink: #1a1a1a;
    --paper-shade: #e9e9e9;
  }
  * { margin: 0; padding: 0; box-sizing: border-box; }
  html, body {
    width: 1200px; height: 900px; overflow: hidden;
    background: var(--backdrop);
  }
  .canvas {
    width: 1200px; height: 900px;
    display: flex; flex-direction: column;
    align-items: center; justify-content: center; gap: 60px;
  }
  .card {
    position: relative;
    width: 600px; height: 343px;
    border: 2px solid var(--gold);
    overflow: hidden;
  }
  .card-texture { position: absolute; inset: 0; }

  /* Front */
  .card--front { background: var(--card-black); }
  .card--front .card-texture {
    background: radial-gradient(ellipse at 40% 50%, #1d1d1d 0%, var(--card-black) 70%);
  }
  .front-brand {
    position: absolute; left: 0; right: 0; top: 128px;
    display: flex; align-items: center; justify-content: center; gap: 18px;
  }
  .brand-dot {
    width: 34px; height: 34px; border-radius: 50%;
    border: 4px solid #fff;
  }
  .brand-name {
    font-family: "Josefin Sans", sans-serif; font-weight: 300;
    letter-spacing: 0.32em; text-transform: uppercase;
  }
  .card--front .brand-name { color: #fff; font-size: 26px; }
  .front-web {
    position: absolute; left: 0; right: 0; top: 210px; text-align: center;
    font-family: "Josefin Sans", sans-serif; font-weight: 400;
    font-size: 13px; letter-spacing: 0.14em; color: var(--gold);
  }

  /* Back */
  .card--back { background: var(--card-white); }
  .card--back .card-texture {
    background: linear-gradient(135deg, #ffffff 0%, var(--paper-shade) 45%, #ffffff 70%, #efefef 100%);
  }
  .back-brand {
    position: absolute; left: 0; right: 0; top: 70px;
    display: flex; align-items: center; justify-content: center; gap: 14px;
  }
  .card--back .brand-dot { width: 26px; height: 26px; border: 3px solid var(--ink); }
  .card--back .brand-name { color: var(--ink); font-size: 19px; }
  .contact {
    position: absolute; font-family: "PT Sans Narrow", sans-serif; color: var(--ink);
  }
  .contact-person { left: 40px; top: 200px; }
  .person-name {
    font-weight: 700; font-size: 20px;
    padding-bottom: 6px; margin-bottom: 10px;
    border-bottom: 1.5px solid var(--ink); width: 180px;
  }
  .contact-row {
    display: flex; align-items: center; gap: 6px;
    font-size: 15px; line-height: 24px;
  }
  .contact-row svg { width: 12px; height: 12px; flex: none; }
  .divider {
    position: absolute; left: 220px; right: 40px; top: 234px;
    height: 1.5px; background: var(--ink);
  }
  .contact-online { right: 40px; top: 248px; }
  .social-dot {
    width: 11px; height: 11px; border: 1.5px solid var(--ink); border-radius: 2px; flex: none;
  }
</style>
</head>
<body>
<main class="canvas">

  <section class="card card--front" aria-label="Card front">
    <div class="card-texture" role="img" aria-label="Faint dark geometric paper texture"></div>
    <div class="front-brand">
      <span class="brand-dot"></span>
      <span class="brand-name">Lanterne architecture</span>
    </div>
    <p class="front-web">www.lanternearchitecture-example.co.nz</p>
  </section>

  <section class="card card--back" aria-label="Card back">
    <div class="card-texture" role="img" aria-label="Soft white embossed geometric texture"></div>
    <div class="back-brand">
      <span class="brand-dot"></span>
      <span class="brand-name">Lanterne architecture</span>
    </div>

    <div class="contact contact-person">
      <p class="person-name">Derek Tolson (Director)</p>
      <p class="contact-row">
        <svg viewBox="0 0 12 12" aria-hidden="true"><circle cx="6" cy="6" r="5.3" fill="none" stroke="#1a1a1a" stroke-width="1.2"/><path d="M4 3.2l1 .2.4 1.4-.7.6a4 4 0 0 0 1.9 1.9l.6-.7 1.4.4.2 1c-2.6.6-5.3-2.1-4.8-4.8z" fill="#1a1a1a"/></svg>
        0279164073
      </p>
      <p class="contact-row">
        <svg viewBox="0 0 12 12" aria-hidden="true"><rect x="0.7" y="2.2" width="10.6" height="7.6" fill="none" stroke="#1a1a1a" stroke-width="1.1"/><path d="M0.9 2.5L6 6.6l5.1-4.1" fill="none" stroke="#1a1a1a" stroke-width="1.1"/></svg>
        info@lanternearchitecture-example.co.nz
      </p>
    </div>

    <div class="divider"></div>

    <div class="contact contact-online">
      <p class="contact-row"><span class="social-dot"></span>@lanternearchitecture</p>
      <p class="contact-row">
        <svg viewBox="0 0 12 12" aria-hidden="true"><circle cx="6" cy="6" r="5.3" fill="none" stroke="#1a1a1a" stroke-width="1.1"/><ellipse cx="6" cy="6" rx="2.3" ry="5.3" fill="none" stroke="#1a1a1a" stroke-width="1"/><path d="M0.8 6h10.4" stroke="#1a1a1a" stroke-width="1"/></svg>
        www.lanternearchitecture-example.co.nz
      </p>
    </div>
  </section>

</main>
</body>
</html>
```